Financial firm simple design

Classic business card design for a financial fund. 2 sided card- white on both sides.. One with just the company name centered and the other w the info. info included on that is :

Name
Company position
phone number
fax
email
website

Financial

```html
<!DOCTYPE html>
<html lang="en">
<head>
<meta charset="utf-8">
<title>Orval Capital — Business Card</title>
<link rel="stylesheet" href="https://fonts.googleapis.com/css2?family=Cinzel:wght@400&family=Source+Sans+3:wght@400&display=swap">
<style>
  :root {
    --backdrop: #e4e6ea;
    --paper: #fbfbfa;
    --navy: #173a66;
    --ink: #2b2b2b;
    --ink-soft: #4a4a4a;
  }
  * { box-sizing: border-box; margin: 0; padding: 0; }
  html, body { width: 1200px; height: 800px; overflow: hidden; }
  body {
    background: var(--backdrop);
    display: flex;
    align-items: center;
    justify-content: center;
    gap: 40px;
  }
  .card {
    position: relative;
    width: 540px;
    height: 309px;
    border-radius: 3px;
    background: var(--paper);
    box-shadow: 0 10px 28px rgba(20, 35, 60, 0.16);
    overflow: hidden;
  }
  .card--back {
    display: flex;
    align-items: center;
    justify-content: center;
  }
  .wordmark {
    font-family: "Cinzel", serif;
    font-weight: 400;
    font-size: 36px;
    letter-spacing: 0.04em;
    color: var(--navy);
    white-space: nowrap;
    line-height: 1;
  }
  .card--front .wordmark {
    position: absolute;
    left: 46px;
    top: 62px;
  }
  .holder {
    position: absolute;
    right: 44px;
    top: 172px;
    text-align: right;
    font-family: "Source Sans 3", sans-serif;
  }
  .holder__name {
    font-size: 21px;
    color: var(--navy);
    letter-spacing: 0.01em;
    line-height: 1.1;
  }
  .holder__role {
    font-size: 13px;
    color: var(--ink);
    margin-top: 2px;
  }
  .contact {
    position: absolute;
    left: 48px;
    bottom: 30px;
    list-style: none;
    font-family: "Source Sans 3", sans-serif;
    font-size: 13.5px;
    line-height: 1.62;
    color: var(--ink-soft);
  }
  .contact__label {
    display: inline-block;
    width: 22px;
    color: var(--navy);
  }
</style>
</head>
<body>
  <section class="card card--front" aria-label="Card front">
    <h1 class="wordmark">Orval Capital</h1>
    <div class="holder">
      <p class="holder__name">DANIEL HARROW</p>
      <p class="holder__role">General Manager</p>
    </div>
    <ul class="contact">
      <li><span class="contact__label">T:</span>(555) 014-2260</li>
      <li><span class="contact__label">F:</span>(555) 014-2261</li>
      <li><span class="contact__label">E:</span>daniel@orvalcapital.com</li>
      <li><span class="contact__label">W:</span>www.orvalcapital.com</li>
    </ul>
  </section>
  <section class="card card--back" aria-label="Card back">
    <p class="wordmark">Orval Capital</p>
  </section>
</body>
</html>
```